Marlo Tidy Yard Website

We need a website design for this new company. I've attached the company logo. This company is in the construction industry that provides general labor, maintenance and cleaning for construction sites. We want a clean and simple website that can be easy to navigate.

Target Market(s)

Construction industry

Industry/Entity Type

Construction

Number of Pages Required

2 page

Font styles to use
Sans Serif

```html
<!DOCTYPE html>
<html lang="en">
<head>
<meta charset="utf-8">
<title>Marlo Tidy Yard</title>
<link rel="stylesheet" href="https://fonts.googleapis.com/css2?family=Montserrat:wght@400;500;600;700;800&display=swap">
<style>
:root{
  --orange:#f26a1b;
  --navy:#1e1d78;
  --ink:#1d1d1d;
  --text:#4a4a4a;
  --grey:#e6e6e6;
  --footer:#0c0c0e;
  --white:#ffffff;
}
*{margin:0;padding:0;box-sizing:border-box}
html,body{width:1200px;height:2672px;overflow:hidden}
body{position:relative;font-family:'Montserrat',sans-serif;color:var(--text);background:var(--white)}
.abs{position:absolute}

/* header */
.site-header{left:0;top:0;width:1200px;height:73px;background:var(--white)}
.brand{left:143px;top:16px;display:flex;align-items:center;gap:7px}
.brand-mark{width:14px;height:14px;background:var(--orange)}
.brand-name{font-size:15px;font-weight:800;color:var(--navy);line-height:1}
.phone-pill{left:928px;top:9px;width:140px;height:31px;border-radius:16px;background:var(--orange);color:var(--white);font-size:14px;font-weight:600;display:flex;align-items:center;justify-content:center;gap:8px}
.main-nav{top:52px;left:0;width:1200px;height:21px}
.main-nav a{position:absolute;top:2px;font-size:11px;font-weight:700;color:var(--ink);text-decoration:none;letter-spacing:.3px;text-transform:uppercase}
.main-nav a.active{border-bottom:2px solid var(--ink);padding-bottom:4px}

/* hero (children positioned relative to the hero box) */
.hero{left:0;top:73px;width:1200px;height:530px;overflow:hidden}
.hero-photo{left:0;top:0;width:1200px;height:523px;background:linear-gradient(120deg,#5d6a76 0%,#3b3a36 35%,#55402e 60%,#2f2b27 100%)}
.hero-shade{left:0;top:0;width:1200px;height:523px;background:rgba(0,0,0,.35)}
.hero-title{left:0;top:161px;width:1200px;text-align:center;color:var(--white);font-size:37px;font-weight:800;letter-spacing:1.5px;line-height:44px}
.hero-text{left:300px;top:264px;width:600px;text-align:center;color:var(--white);font-size:14.5px;line-height:18px}
.btn{left:527px;top:329px;width:145px;height:37px;background:var(--orange);color:var(--white);font-size:12.5px;font-weight:700;display:flex;align-items:center;justify-content:center;letter-spacing:.5px}
.slide-arrow{width:30px;height:30px;background:rgba(40,40,40,.7);display:flex;align-items:center;justify-content:center}

/* section headings */
.section-title{left:0;width:1200px;display:flex;justify-content:center;align-items:center;gap:8px;font-size:25px;font-weight:800;color:var(--ink);text-transform:uppercase}
.section-title .tag{background:var(--orange);color:var(--white);padding:3px 10px}
.section-title.on-dark{color:var(--white)}
.lead{left:211px;width:790px;text-align:center;font-size:11.5px;line-height:24px;color:var(--text)}
.lead.on-dark{color:#d8d8ef}

/* services */
.services{left:0;top:848px;width:1200px;height:556px;background:var(--navy)}
.service{width:240px;text-align:center}
.service-label{margin-top:18px;color:var(--white);font-size:14px;font-weight:700;text-transform:uppercase}

/* projects */
.project{width:222px;height:189px}
.project-photo{width:222px;height:189px}
.project-caption{left:0;bottom:0;width:222px;height:37px;background:rgba(20,20,20,.85);color:var(--white);font-size:11px;font-weight:600;display:flex;align-items:center;padding-left:13px;gap:8px}

/* testimonials */
.testimonials{left:0;top:1839px;width:1200px;height:460px;background:var(--grey)}
.card{width:240px;height:162px;background:var(--white);border:1px solid #cfcfcf;border-radius:14px;text-align:center;padding:40px 22px 0}
.card p{font-size:11px;line-height:20px;color:#666}
.card .who{margin-top:14px;font-size:11.5px;font-weight:700;color:var(--ink)}
.quote-badge{left:50%;top:-20px;margin-left:-22px;width:44px;height:44px;border-radius:50%;background:var(--white);color:var(--orange);font-size:30px;font-weight:800;display:flex;align-items:center;justify-content:center;line-height:1}
.round-arrow{width:22px;height:22px;border-radius:50%;background:#8b8b8b;display:flex;align-items:center;justify-content:center}

/* footer */
.footer{left:0;top:2239px;width:1200px;height:433px}
.footer-head{font-size:11px;font-weight:700;color:var(--white);text-transform:uppercase}
.footer-links{list-style:none}
.footer-links li{font-size:10.5px;font-weight:600;color:var(--white);text-transform:uppercase;line-height:25.5px}
.contact-row{display:flex;gap:14px;font-size:11px;color:#ddd;line-height:20px}
.social{display:flex;gap:10px}
.social span{width:18px;height:18px;border-radius:50%;background:#5b6fb8}
.map{left:758px;top:2349px;width:310px;height:213px;background:linear-gradient(135deg,#e9e5dc,#d7e3c8 55%,#c9dbe9);border:4px solid var(--white)}
.copyright{left:0;width:1200px;text-align:center;font-size:11px;color:#cfcfcf}
</style>
</head>
<body>

<header class="site-header abs">
  <div class="brand abs"><span class="brand-mark"></span><span class="brand-name">Marlo Tidy Yard</span></div>
  <div class="phone-pill abs">
    <svg width="12" height="12" viewBox="0 0 24 24" fill="#fff"><path d="M6.6 10.8c1.4 2.8 3.8 5.1 6.6 6.6l2.2-2.2c.3-.3.7-.4 1-.2 1.1.4 2.3.6 3.6.6.6 0 1 .4 1 1V20c0 .6-.4 1-1 1C10.6 21 3 13.4 3 4c0-.6.4-1 1-1h3.5c.6 0 1 .4 1 1 0 1.3.2 2.5.6 3.6.1.3 0 .7-.2 1z"/></svg>
    555.014.272
  </div>
  <nav class="main-nav abs">
    <a class="active" style="left:596px">Home</a>
    <a style="left:662px">About Us</a>
    <a style="left:752px">Areas We Serve</a>
    <a style="left:888px">Our Projects</a>
    <a style="left:1009px">Contact</a>
  </nav>
</header>

<section class="hero abs" aria-label="Hero">
  <div class="hero-photo abs" role="img" aria-label="Worker in a hard hat cleaning a building facade on scaffolding"></div>
  <div class="hero-shade abs"></div>
  <svg class="abs" style="left:0;top:437px" width="1200" height="93" viewBox="0 0 1200 93">
    <polygon points="0,13 600,86 1200,13 1200,93 0,93" fill="#fff"/>
    <polygon points="0,13 600,86 1200,13 1200,22 600,93 0,22" fill="#f26a1b"/>
  </svg>
  <h1 class="hero-title abs">COMPREHENSIVE PORT-<br>CONSTRUCTION CLEANING</h1>
  <p class="hero-text abs">Must explain to you how all this mistaken idea of denouncing pleasure and praising pain was born and I will give you a completed.</p>
  <div class="btn abs">MORE DETAILS</div>
  <div class="slide-arrow abs" style="left:86px;top:209px"><svg width="8" height="12" viewBox="0 0 8 12"><path d="M6 1 1 6l5 5" stroke="#fff" stroke-width="2" fill="none"/></svg></div>
  <div class="slide-arrow abs" style="left:1086px;top:209px"><svg width="8" height="12" viewBox="0 0 8 12"><path d="M2 1l5 5-5 5" stroke="#fff" stroke-width="2" fill="none"/></svg></div>
</section>

<section aria-label="Welcome">
  <h2 class="section-title abs" style="top:641px">Welcome to <span class="tag">Marlo Tidy Yard</span></h2>
  <p class="lead abs" style="top:704px">Lorem ipsum dolor sit amet, consectetur adipiscing elit, sed do eiusmod tempor incididunt ut labore et dolore magna aliqua. Ut enim ad minim veniam, quis nostrud exercitation ullamco laboris nisi ut aliquip ex ea commodo consequat. Duis aute irure dolor in reprehenderit in voluptate velit esse cillum dolore eu fugiat nulla pariatur. Excepteur sint occaecat cupidatat non proident, sunt in culpa qui officia deserunt mollit anim id est laborum.</p>
</section>

<section class="services abs" aria-label="Our services">
  <div class="abs" style="left:0;top:0;width:1200px;height:556px;background:linear-gradient(90deg,rgba(255,255,255,.04),rgba(255,255,255,.1))" role="img" aria-label="Faint construction site backdrop"></div>
  <h2 class="section-title on-dark abs" style="top:48px">Our <span class="tag">Services</span></h2>
  <p class="lead on-dark abs" style="top:109px">Lorem ipsum dolor sit amet, consectetur adipiscing elit, sed do eiusmod tempor incididunt ut labore et dolore magna aliqua. Ut enim ad minim veniam, quis nostrud exercitation ullamco laboris nis</p>

  <div class="service abs" style="left:150px;top:194px">
    <svg width="240" height="260" viewBox="0 0 240 260" role="img" aria-label="Labourers cutting materials on site">
      <polygon points="120,4 232,66 232,194 120,256 8,194 8,66" fill="#f26a1b"/>
      <polygon points="120,12 224,71 224,189 120,248 16,189 16,71" fill="#a98f74"/>
    </svg>
    <div class="service-label">Labour</div>
  </div>
  <div class="service abs" style="left:497px;top:194px">
    <svg width="240" height="260" viewBox="0 0 240 260" role="img" aria-label="Hand tools laid out on a workbench">
      <polygon points="120,4 232,66 232,194 120,256 8,194 8,66" fill="#f26a1b"/>
      <polygon points="120,12 224,71 224,189 120,248 16,189 16,71" fill="#8a5a36"/>
    </svg>
    <div class="service-label">Maintenance</div>
  </div>
  <div class="service abs" style="left:823px;top:194px">
    <svg width="240" height="260" viewBox="0 0 240 260" role="img" aria-label="Worker pressure washing a concrete floor">
      <polygon points="120,4 232,66 232,194 120,256 8,194 8,66" fill="#f26a1b"/>
      <polygon points="120,12 224,71 224,189 120,248 16,189 16,71" fill="#b7b6b0"/>
    </svg>
    <div class="service-label">Cleaning</div>
  </div>
</section>

<section aria-label="Our projects">
  <h2 class="section-title abs" style="top:1443px">Our <span class="tag">Projects</span></h2>
  <p class="lead abs" style="top:1504px">Lorem ipsum dolor sit amet, consectetur adipiscing elit, sed do eiusmod tempor incididunt ut labore et dolore magna aliqua. Ut enim ad minim veniam, quis nostrud exercitation ullamco laboris nisi ut aliquip ex ea commodo</p>

  <div class="project abs" style="left:132px;top:1584px">
    <div class="project-photo" role="img" aria-label="Crew working beside an excavator" style="background:linear-gradient(160deg,#c9a24a,#7d7358)"></div>
    <div class="project-caption abs">Post cleaning work <span>»</span></div>
  </div>
  <div class="project abs" style="left:371px;top:1584px">
    <div class="project-photo" role="img" aria-label="Site workers in hard hats" style="background:linear-gradient(160deg,#b9c7d6,#51698a)"></div>
    <div class="project-caption abs">Post cleaning work <span>»</span></div>
  </div>
  <div class="project abs" style="left:607px;top:1584px">
    <div class="project-photo" role="img" aria-label="Engineers reviewing plans on site" style="background:linear-gradient(160deg,#a7a49a,#5c5a4f)"></div>
    <div class="project-caption abs">Post cleaning work <span>»</span></div>
  </div>
  <div class="project abs" style="left:846px;top:1584px">
    <div class="project-photo" role="img" aria-label="Worker laying bricks" style="background:linear-gradient(160deg,#9fb6cc,#8a6a4a)"></div>
    <div class="project-caption abs">Post cleaning work <span>»</span></div>
  </div>
</section>

<section class="testimonials abs" aria-label="Client testimonials">
  <h2 class="section-title abs" style="top:57px">Client <span class="tag">Testimonials</span></h2>
  <div class="round-arrow abs" style="left:138px;top:235px"><svg width="6" height="10" viewBox="0 0 6 10"><path d="M5 1 1 5l4 4" stroke="#fff" stroke-width="1.6" fill="none"/></svg></div>
  <div class="round-arrow abs" style="left:1044px;top:235px"><svg width="6" height="10" viewBox="0 0 6 10"><path d="M1 1l4 4-4 4" stroke="#fff" stroke-width="1.6" fill="none"/></svg></div>

  <div class="card abs" style="left:189px;top:179px">
    <div class="quote-badge abs">“</div>
    <p>Lorem ipsum dolor sit amet, consectetuer adipiscing elit. Aenean commodo ligula eget dolor. ligula eget dolor.</p>
    <div class="who">Rowan Whitfield</div>
  </div>
  <div class="card abs" style="left:483px;top:179px">
    <div class="quote-badge abs">“</div>
    <p>Lorem ipsum dolor sit amet, consectetuer adipiscing elit. Aenean commodo ligula eget dolor. ligula eget dolor.</p>
    <div class="who">Celia Marbrook</div>
  </div>
  <div class="card abs" style="left:771px;top:173px">
    <div class="quote-badge abs">“</div>
    <p>Lorem ipsum dolor sit amet, consectetuer adipiscing elit. Aenean commodo ligula eget dolor. ligula eget dolor.</p>
    <div class="who">Tomas Greer</div>
  </div>
</section>

<footer class="footer abs">
  <svg class="abs" style="left:0;top:0" width="1200" height="433" viewBox="0 0 1200 433">
    <polygon points="0,57 600,0 1200,57 1200,433 0,433" fill="#f26a1b"/>
    <polygon points="0,66 600,8 1200,66 1200,433 0,433" fill="#0c0c0e"/>
  </svg>
  <div class="abs" style="left:0;top:120px;width:1200px;height:313px;background:linear-gradient(180deg,rgba(40,40,48,0),rgba(40,40,48,.6))" role="img" aria-label="Faint city skyline silhouette"></div>

  <div class="abs" style="left:150px;top:118px">
    <div class="footer-head">Quick Links</div>
    <ul class="footer-links" style="margin-top:10px">
      <li>Home</li><li>What We Do</li><li>Our Products</li><li>Areas We Serve</li><li>About</li><li>Contact Us</li>
    </ul>
  </div>

  <div class="abs" style="left:367px;top:118px">
    <div class="footer-head">Contact Us</div>
    <div class="contact-row" style="margin-top:18px">
      <svg width="12" height="16" viewBox="0 0 12 16" style="margin-top:3px"><path d="M6 0a6 6 0 0 0-6 6c0 4.5 6 10 6 10s6-5.5 6-10a6 6 0 0 0-6-6zm0 8.5A2.5 2.5 0 1 1 6 3.5a2.5 2.5 0 0 1 0 5z" fill="#ddd"/></svg>
      <span>418 Harbor Lane<br>Fenwick, TX 75001</span>
    </div>
    <div class="contact-row" style="margin-top:40px">
      <svg width="14" height="14" viewBox="0 0 24 24" style="margin-top:3px"><path d="M6.6 10.8c1.4 2.8 3.8 5.1 6.6 6.6l2.2-2.2c.3-.3.7-.4 1-.2 1.1.4 2.3.6 3.6.6.6 0 1 .4 1 1V20c0 .6-.4 1-1 1C10.6 21 3 13.4 3 4c0-.6.4-1 1-1h3.5c.6 0 1 .4 1 1 0 1.3.2 2.5.6 3.6.1.3 0 .7-.2 1z" fill="#ddd"/></svg>
      <span>+1 555 014 273</span>
    </div>
    <div class="contact-row" style="margin-top:30px">
      <svg width="14" height="11" viewBox="0 0 14 11" style="margin-top:5px"><rect x="0" y="0" width="14" height="11" fill="#ddd"/><path d="M0 0l7 6 7-6" stroke="#0c0c0e" stroke-width="1.3" fill="none"/></svg>
      <span>hello@marlotidyyard.com</span>
    </div>
  </div>

  <div class="abs" style="left:569px;top:118px">
    <div class="footer-head">Social Links</div>
    <div class="social" style="margin-top:20px"><span></span><span></span><span></span><span></span></div>
  </div>

  <p class="copyright abs" style="top:401px">©2019 marlotidyyard.com. All Rights Reserved</p>
</footer>
<div class="map abs" role="img" aria-label="Street map showing the office location"></div>

</body>
</html>
```